Packing for Disinfectant wipes

Design the Packinging for new Disinfectant wipes. Wipes are for cleaning and disinfectanting hard surfaces and equipment. There are 100 wipes to the packet (size 230mm x 300mm). The company is called Norbeck Supplies and is supplier of consumable products to healthcare companies. Wipes are not for use on humans/baby. Packaging size as per attachment.
Industry/Entity Type
Healthcare
Requirements
Nice to have
- Packaging need ingredients list and directions for use

```html
<!DOCTYPE html>
<html lang="en">
<head>
<meta charset="utf-8">
<title>Norbeck Supplies Disinfectant Wipes Packaging</title>
<link href="https://fonts.googleapis.com/css2?family=Montserrat:ital,wght@0,400;0,500;0,600;0,700;0,800;1,800&family=Poppins:wght@400;600;700&display=swap" rel="stylesheet">
<style>
:root{
  --backdrop:#7fbccb;
  --ink:#1f2a33;
  --slate:#3a4650;
  --leaf:#6aaf44;
  --lime:#b5c93a;
  --sky:#3d8fc6;
  --amber:#e0842e;
  --seal:#eceef0;
  --seal-line:#c9ced3;
  --paper:#f6f7f8;
}
*{margin:0;padding:0;box-sizing:border-box}
html,body{width:1200px;height:866px;overflow:hidden}
body{background:var(--backdrop);position:relative;font-family:"Montserrat",sans-serif;color:var(--ink)}

.pack{position:absolute;left:299px;width:599px;overflow:hidden}
.pack--front{top:138px;height:276px;
  background:linear-gradient(90deg,var(--paper) 0 16%,var(--leaf) 28%,var(--lime) 40%,#7fb4a0 52%,var(--sky) 62%,#e7d8c4 74%,#e9b27a 86%,var(--amber) 100%)}
.pack--back{top:459px;height:285px;
  background:linear-gradient(90deg,var(--paper) 0 8%,#f2e6d8 22%,#f0cfa8 38%,#f5f5f0 55%,#cfe0ec 62%,var(--sky) 72%,#5aa24a 84%,var(--leaf) 94%,var(--lime) 100%)}

.panel-shape{position:absolute;inset:0;width:100%;height:100%}

.seal{position:absolute;top:0;bottom:0;width:34px;
  background:repeating-linear-gradient(90deg,var(--seal) 0 4px,var(--seal-line) 4px 5px);opacity:.92}
.seal--left{left:0}
.seal--right{right:0;background:repeating-linear-gradient(90deg,rgba(255,255,255,.35) 0 4px,rgba(0,0,0,.12) 4px 5px)}

.count{position:absolute;left:44px;top:22px;line-height:1}
.count__number{font-family:"Poppins",sans-serif;font-weight:700;font-size:15px;display:block}
.count__label{font-family:"Poppins",sans-serif;font-weight:400;font-size:12px;display:block;margin-top:2px}

.usage-note{position:absolute;left:-18px;top:190px;width:140px;transform:rotate(-90deg);transform-origin:center;
  font-family:"Poppins",sans-serif;font-size:3.6px;line-height:5px;color:var(--slate)}

.lid{position:absolute;left:166px;top:57px;width:267px;height:159px;border-radius:46px;
  background:#fbfbfb;box-shadow:0 3px 6px rgba(0,0,0,.25);padding:12px}
.lid__tab{position:absolute;left:86px;top:-3px;width:96px;height:8px;background:#f0f0f0;border-radius:3px;box-shadow:0 1px 2px rgba(0,0,0,.2)}
.lid__tab--bottom{top:auto;bottom:-3px;left:112px;width:40px}
.lid__window{width:100%;height:100%;border-radius:36px;
  background:linear-gradient(100deg,#9fc96a 0%,#dfe8d6 45%,#eef1f3 70%,#f2dcc4 100%);
  display:flex;flex-direction:column;align-items:center;padding-top:26px}
.brand{font-weight:500;font-size:13px;color:var(--slate);letter-spacing:.2px}
.product{font-weight:800;font-style:italic;font-size:33px;color:var(--ink);margin-top:6px;line-height:1;letter-spacing:-.5px}
.product__band{margin-top:2px;width:200px;height:17px;
  background:linear-gradient(90deg,rgba(224,132,46,.2),var(--amber) 20%,var(--amber) 80%,rgba(224,132,46,.2));
  color:#fff;font-weight:700;font-size:15px;text-align:center;line-height:17px}

.directions{position:absolute;left:0;right:0;top:8px;text-align:center}
.directions__title{font-weight:400;font-size:9px;color:var(--slate);letter-spacing:.2px}
.directions__steps{display:flex;justify-content:center;gap:40px;margin-top:6px}
.step-icon{width:20px;height:18px;border:1px solid var(--slate);border-radius:3px;opacity:.7}

.first-aid{position:absolute;left:130px;right:130px;top:50px;text-align:center;font-family:"Poppins",sans-serif}
.first-aid__title{font-weight:700;font-size:7px;color:var(--ink);margin-bottom:2px}
.first-aid h4{font-size:3.4px;font-weight:600;line-height:4.6px}
.first-aid p{font-size:3.4px;line-height:4.6px;color:#333}

.reseal{position:absolute;left:0;right:0;top:117px;height:42px;
  background:repeating-linear-gradient(180deg,rgba(255,255,255,.55) 0 3px,rgba(0,0,0,.07) 3px 5px,rgba(255,255,255,.2) 5px 8px)}

.ingredients{position:absolute;left:184px;top:186px;width:232px}
.ingredients__title{font-size:4.6px;font-weight:600;color:var(--ink);margin-bottom:4px}
.ingredients table{width:100%;border-collapse:collapse;font-size:5px;color:var(--ink)}
.ingredients th,.ingredients td{border:.5px solid #5a6670;padding:0 2px;height:7.6px;text-align:left;font-weight:400}
.ingredients th{font-size:3.6px;font-weight:600}
.ingredients .col-name{width:45%}
.ingredients .col-cas{width:23%}
</style>
</head>
<body>

<section class="pack pack--front" aria-label="Front of packet">
  <svg class="panel-shape" viewBox="0 0 599 276" preserveAspectRatio="none" aria-hidden="true">
    <path d="M0 0 H260 C170 20 100 110 92 276 H0 Z" fill="var(--paper)"/>
  </svg>
  <div class="seal seal--left"></div>
  <div class="seal seal--right"></div>

  <div class="count">
    <span class="count__number">100 wipes</span>
    <span class="count__label">disinfectant</span>
  </div>
  <p class="usage-note">For cleaning and disinfectanting hard surfaces and equipment.<br>Not for use on humans.</p>

  <div class="lid">
    <span class="lid__tab"></span>
    <div class="lid__window">
      <span class="brand">Norbeck Supplies</span>
      <span class="product">Disinfectant</span>
      <span class="product__band">WIPES</span>
    </div>
    <span class="lid__tab lid__tab--bottom"></span>
  </div>
</section>

<section class="pack pack--back" aria-label="Back of packet">
  <div class="seal seal--left"></div>
  <div class="seal seal--right"></div>

  <div class="directions">
    <h2 class="directions__title">DIRECTIONS OF USE</h2>
    <div class="directions__steps">
      <span class="step-icon" role="img" aria-label="Step 1: pull a wipe from the packet"></span>
      <span class="step-icon" role="img" aria-label="Step 2: wipe the hard surface"></span>
      <span class="step-icon" role="img" aria-label="Step 3: leave the surface to dry"></span>
    </div>
  </div>

  <div class="first-aid">
    <h3 class="first-aid__title">FIRST-AID MEASURES</h3>
    <h4>Inhalation:</h4>
    <p>Move person to fresh air and keep at rest. If breathing is irregular, give oxygen by trained staff. Get medical attention if symptoms occur. Symptoms may be delayed, so keep the person under observation for 48 hours.</p>
    <h4>Ingestion:</h4>
    <p>Rinse mouth with water. If swallowed and the person is conscious, give small amounts of water to drink. Do not induce vomiting unless told to by medical staff.</p>
    <h4>Skin contact:</h4>
    <p>Flush skin with plenty of water. Remove contaminated clothing and shoes. Get medical attention if symptoms occur.</p>
    <h4>Eye contact:</h4>
    <p>Flush eyes with plenty of water, lifting the upper and lower eyelids. Remove contact lenses. Rinse for at least 10 minutes. Get medical attention if irritation occurs.</p>
  </div>

  <div class="reseal"></div>

  <div class="ingredients">
    <h3 class="ingredients__title">INFORMATION ON INGREDIENTS</h3>
    <table>
      <tr><th class="col-name">INGREDIENT</th><th class="col-cas">CAS NUMBER</th><th>FUNCTION</th></tr>
      <tr><td>AQUA</td><td>7732-18-5</td><td>Solvent</td></tr>
      <tr><td>Didecyldimethylammonium chloride</td><td>7173-51-5</td><td>Antioxidant</td></tr>
      <tr><td>Benzalkonium Chloride</td><td>68424-85-1</td><td>Antioxidant</td></tr>
      <tr><td>Phenoxyethanol</td><td>122-99-6</td><td>preservation</td></tr>
      <tr><td>PEG40 Hydrogenated Casor Oil</td><td>61788-85-0</td><td>Surfactant</td></tr>
      <tr><td>Ethylhexylglycerin</td><td>70445-33-9</td><td>Solvent</td></tr>
      <tr><td>Disodium EDTA</td><td>139-33-3</td><td>Chelating agents</td></tr>
      <tr><td>Perfume</td><td>N/A</td><td>Fragrance</td></tr>
    </table>
  </div>
</section>

</body>
</html>
```